Web tool bar Project

I'm open to paying more if the quality of the bar is very good... if you feel the scope of the project does not match budget..... please quote me.

I need someone to re-design my web tool bar.

In the first attachment you can see a black tool bar (fig1). This is my old design. I want this to be the template as it shows what the text will say and where the buttons will be placed.

For the new tool bar:
-I would like the it to be white in colour (like fig.2)
-I would like the buttons to also be white. But the buttons must stand out so the designer should use the right shading to make the buttons stand out.
-The bar needs to be the quality of the bar in fig.2 (very good quality). I have had many designs done for this but no designer seems to be good enough to get the right quality.
-The text in the white boxes on the new bar should be the colours shown above the buttons next to fig.1 (blue, green, red, yellow, purple & orange).

Finally please put the logo attached (QT) at the end of the bar on the right where it says logo. The logo should blend in well with the bar as it has white in it also.

Please take note of fig.2 it is good quality with sharp edges I would like the same quality.

Any further questions please ask?

Requirements
Must have
• Quality!

```html
<!DOCTYPE html>
<html lang="en">
<head>
<meta charset="utf-8">
<title>Quiet Terrace toolbar</title>
<link href="https://fonts.googleapis.com/css2?family=Arimo:wght@400&display=swap" rel="stylesheet">
<style>
  :root {
    --page: #ffffff;
    --bar-top: #ffffff;
    --bar-bottom: #ececec;
    --bar-edge: #dedede;
    --btn-top: #ffffff;
    --btn-bottom: #f3f3f3;
    --btn-border: #e1e1e1;
    --divider: #e4e4e4;
    --blue: #1a9bd7;
    --green: #8cc43c;
    --red: #e8343c;
    --yellow: #f2c41f;
    --purple: #c0106c;
    --orange: #f26a3d;
  }
  * { box-sizing: border-box; margin: 0; padding: 0; }
  html, body { width: 1200px; height: 94px; overflow: hidden; background: var(--page); }
  body { font-family: "Arimo", Arial, sans-serif; font-size: 12.5px; position: relative; }

  .toolbar {
    position: absolute; left: 0; top: 0; width: 1200px; height: 62px;
    background: linear-gradient(var(--bar-top), var(--bar-bottom));
    border-bottom: 1px solid var(--bar-edge);
    box-shadow: 0 2px 3px rgba(0,0,0,0.06);
  }
  .tool {
    position: absolute; top: 8px; height: 42px;
    display: flex; align-items: stretch;
    background: linear-gradient(var(--btn-top), var(--btn-bottom));
    border: 1px solid var(--btn-border);
    border-radius: 3px;
    box-shadow: 0 1px 2px rgba(0,0,0,0.12), inset 0 1px 0 #fff;
  }
  .tool-item {
    display: flex; align-items: center; justify-content: center; gap: 7px;
    white-space: nowrap; padding: 0 8px;
  }
  .tool-item + .tool-item { border-left: 1px solid var(--divider); }
  .tool-item svg { width: 17px; height: 17px; flex: none; }

  .tool-login   { left: 162px; width: 150px; }
  .tool-social  { left: 350px; width: 270px; }
  .tool-social .tool-item:first-child { width: 92px; }
  .tool-social .tool-item:last-child { flex: 1; }
  .tool-feeds   { left: 629px; width: 117px; }
  .tool-messages{ left: 755px; width: 98px; }
  .tool-scrapbook { left: 862px; width: 96px; }

  .c-blue { color: var(--blue); }
  .c-green { color: var(--green); }
  .c-red { color: var(--red); }
  .c-yellow { color: var(--yellow); }
  .c-purple { color: var(--purple); }
  .c-orange { color: var(--orange); }

  .brand {
    position: absolute; left: 990px; top: 18px; height: 22px;
    display: flex; align-items: center; gap: 6px;
    color: var(--blue); font-size: 17px;
  }
  .brand-square { width: 16px; height: 16px; background: var(--blue); border-radius: 2px; }
</style>
</head>
<body>
  <nav class="toolbar">
    <div class="tool tool-login">
      <span class="tool-item c-blue">
        <svg viewBox="0 0 18 18" fill="none" stroke="currentColor" stroke-width="1.6"><rect x="3" y="8" width="12" height="9" rx="1"/><path d="M5.5 8V5.5a3.5 3.5 0 0 1 7 0V8"/><path d="M9 11.5v2"/></svg>
        Quiet Terrace login
      </span>
    </div>

    <div class="tool tool-social">
      <span class="tool-item c-green">
        <svg viewBox="0 0 18 18" fill="none" stroke="currentColor" stroke-width="1.6"><path d="M13 9.5V16H2V4h7"/><path d="M7 11l1-3 7-7 2 2-7 7z"/></svg>
        Check-in
      </span>
      <span class="tool-item c-red">
        <svg viewBox="0 0 18 18" fill="none" stroke="currentColor" stroke-width="1.6"><circle cx="9" cy="5.5" r="3.8"/><path d="M2.5 17v-2a4 4 0 0 1 4-4h5a4 4 0 0 1 4 4v2z"/></svg>
        Online friends at Circlenet
      </span>
    </div>

    <div class="tool tool-feeds">
      <span class="tool-item c-yellow">
        <svg viewBox="0 0 18 18" fill="currentColor"><circle cx="3.5" cy="14.5" r="2"/><path d="M1.5 7.5a9 9 0 0 1 9 9h-2.5a6.5 6.5 0 0 0-6.5-6.5z"/><path d="M1.5 1.5a15 15 0 0 1 15 15H14A12.5 12.5 0 0 0 1.5 4z"/></svg>
        Lounge feeds
      </span>
    </div>

    <div class="tool tool-messages">
      <span class="tool-item c-purple">
        <svg viewBox="0 0 18 18" fill="none" stroke="currentColor" stroke-width="1.6"><rect x="1.5" y="3.5" width="15" height="11"/><path d="M1.5 3.5L9 10l7.5-6.5M1.5 14.5l5.5-5M16.5 14.5l-5.5-5"/></svg>
        Messages
      </span>
    </div>

    <div class="tool tool-scrapbook">
      <span class="tool-item c-orange">
        <svg viewBox="0 0 18 18" fill="none" stroke="currentColor" stroke-width="1.6"><rect x="3" y="1.5" width="12" height="15" rx="1"/><path d="M6 1.5v15"/></svg>
        Scapbook
      </span>
    </div>

    <div class="brand">
      <span class="brand-square"></span>
      <span class="brand-name">QT</span>
    </div>
  </nav>
</body>
</html>
```